Calloway Brothers Civil Construction website design

We want a Bold website to promote our Heavy Civil Construction company, We would like an organic / tangible feel to the site. The pictures will be over saturated so they pop. We need to be able to easliy upload new projects and pictures on a regular basis.
Home page will have a full screen width image, "home page image" with silhouette and logo. It will also have about us area and picture
Page 2 will be Project Gallery with pictures in project folders
Page 3 will be an employment application form and submission
Page 4 will be Contact Us
Construction indusrty
Contractor
Coded - Design and coding required
4 page
- Hypatia Sans Pro Light

```html
<!DOCTYPE html>
<html lang="en">
<head>
<meta charset="utf-8">
<title>Calloway Brothers Civil Construction</title>
<link rel="stylesheet" href="https://fonts.googleapis.com/css2?family=Montserrat:wght@300;400;500;600;700&family=Open+Sans:wght@400;600&display=swap">
<style>
:root{
  --blue:#3654a8;
  --blue-soft:#8e9fd2;
  --grey:#8f8f8f;
  --frame:#ececec;
  --ink:#1e1e1e;
  --night:#0f111a;
  --white:#ffffff;
}
*{margin:0;padding:0;box-sizing:border-box}
html,body{width:1200px;height:2234px;overflow:hidden;background:var(--white)}
body{position:relative;font-family:"Montserrat",sans-serif;color:var(--ink)}
.abs{position:absolute}
.shapes{position:absolute;left:0;top:0;width:1200px;height:2234px}

.hero{left:0;top:0;width:1200px;height:622px;
  background:linear-gradient(180deg,#dfe6f1 0%,#eef2f8 40%,#c9cfdb 74%,#2b3040 86%,#07080c 100%)}
.menu-btn{left:1068px;top:23px;width:33px;height:33px;background:#d9dce2;border-radius:3px}
.menu-btn span{position:absolute;left:8px;width:17px;height:2px;background:#8b8f97}
.hero-name{left:200px;top:195px;width:800px;color:var(--blue);font-weight:600;line-height:1}
.hero-name .mark{position:absolute;left:0;top:4px;width:140px;height:140px;border:14px solid var(--blue)}
.hero-name .line1{position:absolute;left:192px;top:16px;font-size:56px;letter-spacing:1px;white-space:nowrap}
.hero-name .line2{position:absolute;left:194px;top:90px;font-size:36px;letter-spacing:13px;white-space:nowrap}
.tagline{left:0;top:570px;width:1200px;text-align:center;color:var(--white);font-weight:600;font-size:33px;letter-spacing:1.5px}

.photo-frame{background:var(--frame);padding:9px}
.photo{width:100%;height:100%}
.about-photo{left:99px;top:708px;width:475px;height:368px}
.about-photo .photo{background:linear-gradient(110deg,#7c8850 0%,#a79a6c 40%,#6f7a77 60%,#9a9fa3 100%)}

.section-title{color:var(--blue);font-weight:700;font-size:34px;letter-spacing:1px}
.rule{width:52px;height:3px;background:var(--grey)}
.about-title{left:600px;top:708px}
.about-rule{left:600px;top:759px}
.about-lead{left:602px;top:796px;width:497px;font-size:14.6px;line-height:23.3px;font-weight:400;text-align:justify}
.about-body{left:602px;top:873px;width:497px;font-size:14.2px;line-height:23.3px;font-weight:300;text-align:justify;color:#333}

.outline-btn{display:flex;align-items:center;border:3px solid var(--blue);color:var(--blue);font-weight:500;font-size:16px;letter-spacing:.5px;background:var(--white)}
.outline-btn .box{width:26px;height:26px;background:var(--grey);margin:0 16px 0 6px;flex:none}
.contact-btn{left:600px;top:1016px;width:244px;height:42px}
.view-btn{left:99px;top:1925px;width:166px;height:42px}

.gallery-title{left:99px;top:1262px}
.gallery-rule{left:99px;top:1311px}
.card{width:317px;height:240px}
.g1 .photo{background:linear-gradient(170deg,#9cc4e6 0%,#8c7a5e 45%,#8a5a3e 75%,#5f7e3e 100%)}
.g2 .photo{background:linear-gradient(180deg,#5d7a3e 0%,#2fa3a3 50%,#9a9070 100%)}
.g3 .photo{background:linear-gradient(180deg,#8dc4ee 0%,#b59f80 50%,#2d5fa8 100%)}
.g4 .photo{background:linear-gradient(180deg,#c8d2d8 0%,#4d6e3a 25%,#a56a44 60%,#8c5a40 100%)}
.g5 .photo{background:linear-gradient(160deg,#7e8a78 0%,#5f7a4e 50%,#a59c8a 100%)}
.g6 .photo{background:linear-gradient(180deg,#c4ccd2 0%,#4d6a3a 40%,#4a4630 70%,#6a8a3e 100%)}

.foot-name{left:690px;top:1918px;color:#c9d2ee;font-weight:600;line-height:1}
.foot-name .mark{position:absolute;left:0;top:4px;width:70px;height:70px;border:7px solid #c9d2ee}
.foot-name .line1{position:absolute;left:98px;top:8px;font-size:28px;white-space:nowrap}
.foot-name .line2{position:absolute;left:99px;top:44px;font-size:17.5px;letter-spacing:6px;white-space:nowrap}

.foot-nav{left:396px;top:2125px;font-family:"Open Sans",sans-serif;font-size:13px;font-weight:600;color:var(--white);display:flex}
.foot-nav a{color:inherit;text-decoration:none}
.copyright{left:0;top:2175px;width:1200px;text-align:center;font-family:"Open Sans",sans-serif;font-size:15px;color:var(--white);letter-spacing:-.3px}
</style>
</head>
<body>
  <header class="hero abs" role="img" aria-label="Evening sky with silhouettes of an excavator, dozer and dump truck on a ridge"></header>
  <div class="menu-btn abs"><span style="top:10px"></span><span style="top:15px"></span><span style="top:20px"></span></div>
  <div class="hero-name abs">
    <div class="mark"></div>
    <div class="line1">CALLOWAY BROTHERS</div>
    <div class="line2">CIVIL CONSTRUCTION</div>
  </div>
  <p class="tagline abs">In Business Since 20 Years</p>

  <svg class="shapes" viewBox="0 0 1200 2234" aria-hidden="true">
    <rect x="0" y="2031" width="1200" height="203" fill="var(--night)"/>
    <polygon points="0,584 280,584 422,1175 0,1175" fill="var(--blue)"/>
    <polygon points="422,1175 1200,1175 1200,2087 642,2087" fill="var(--blue)"/>
  </svg>

  <section class="about">
    <div class="about-photo photo-frame abs"><div class="photo" role="img" aria-label="Aerial view of a multi-lane highway beside a drainage channel and wetland"></div></div>
    <h2 class="section-title about-title abs">ABOUT US</h2>
    <div class="rule about-rule abs"></div>
    <p class="about-lead abs">Lorem ipsum dolor sit amet, consectetuer adipiscing elit, sed diammagna nonummy nibh euismod tincidunt ut laoreet dolore magna aliqua</p>
    <p class="about-body abs">Lorem ipsum dolor sit amet, consectetuer adipiscing elit, sed diam nonummy nibh euismod tincidunt ut laoreet dolore magna aliquam erat volutpat. Ut wisi enim ad minim veniam, quis nostrud exerci tation ullamcorper suscipit lobortis nisl ut aliquip ex ea commodo consequat. Duis autem ve.</p>
    <a class="outline-btn contact-btn abs"><span class="box"></span>CONTACT US TODAY</a>
  </section>

  <section class="gallery">
    <h2 class="section-title gallery-title abs">GALLERY</h2>
    <div class="rule gallery-rule abs"></div>
    <div class="card photo-frame g1 abs" style="left:99px;top:1366px"><div class="photo" role="img" aria-label="Excavators digging a channel behind homes"></div></div>
    <div class="card photo-frame g2 abs" style="left:442px;top:1366px"><div class="photo" role="img" aria-label="Worker hydroseeding a reinforced bank above water"></div></div>
    <div class="card photo-frame g3 abs" style="left:785px;top:1366px"><div class="photo" role="img" aria-label="Equipment building a rock shoreline at a lake"></div></div>
    <div class="card photo-frame g4 abs" style="left:99px;top:1632px"><div class="photo" role="img" aria-label="Excavator loading articulated dump trucks on cleared land"></div></div>
    <div class="card photo-frame g5 abs" style="left:442px;top:1632px"><div class="photo" role="img" aria-label="Aerial view of a site with retention pond and buildings"></div></div>
    <div class="card photo-frame g6 abs" style="left:785px;top:1632px"><div class="photo" role="img" aria-label="Pond with a finished rock-lined bank and lawn"></div></div>
    <a class="outline-btn view-btn abs"><span class="box"></span>VIEW ALL</a>
  </section>

  <div class="foot-name abs">
    <div class="mark"></div>
    <div class="line1">CALLOWAY BROTHERS</div>
    <div class="line2">CIVIL CONSTRUCTION</div>
  </div>

  <footer>
    <nav class="foot-nav abs">
      <a style="margin-right:36px">HOME</a>
      <a style="margin-right:36px">PROJECT GALLERY</a>
      <a style="margin-right:48px">CAREERS</a>
      <a>CONTACT US</a>
    </nav>
    <p class="copyright abs">Copyright © 2019 Calloway Brothers Civil Construction. All Rights Reserved.</p>
  </footer>
</body>
</html>
```